Wordpress Design Project - Team Korvel BE

We currently have a Blogger themed blog to capture our cycling teams trials and tribulations. (www.teamkorvel-example.be). We want this migrated to a wordpress theme and a proper-clean-no-clutter layout done for the blog.

We need to have a couple of design elements incorporated into the overall design. (e.g twitter feeds, weather forecasts, calendar with upcoming events of the team, and we need to allow each member of the team to add blog entries).

It is essential that the overall design of the blog-layout remain very clean, but well integrated!

Regards,
/TeamKorvel

PS. Some of the existing design elements need to remain.

Industry/Entity Type

Events

Requirements
Must have
• Social Feed - both feeds from people we follow and our own twitter updates need to appear here
weather forecast - for next few days of our region
calander for upcomming events of the team - and overview of team mates holidays (which they add themselves, overlaid)
access for all members to add blog entries, foto's, video, comments on blog posts...

somewhere on the right hand side of the blog, the sponsors logo's muct appear... I want to be able to change these if we get new sponsors...

"like us on Facebook" link needed as well.

```html
<!DOCTYPE html>
<html lang="en">
<head>
<meta charset="utf-8">
<title>Team Korvel</title>
<link href="https://fonts.googleapis.com/css2?family=Ubuntu:wght@300;400;500&family=Source+Sans+3:ital,wght@0,400;0,600;1,400;1,600&display=swap" rel="stylesheet">
<style>
:root{
  --dark:#1c1c1c;
  --dark-2:#2a2a2a;
  --page:#ececec;
  --card:#ffffff;
  --red:#e8141c;
  --cal-red:#a80d25;
  --cal-border:#d21a34;
  --yellow:#f3b81a;
  --text:#3a3a3a;
  --muted:#8a8a8a;
  --panel-head:#d9d9d9;
  --foot-text:#d8d8d8;
  --foot-muted:#8c8c8c;
}
*{box-sizing:border-box;margin:0;padding:0}
html,body{width:1200px;height:2323px;overflow:hidden}
body{position:relative;background:var(--page);font-family:"Source Sans 3",sans-serif;color:var(--text)}
.abs{position:absolute}

/* header */
.site-header{left:0;top:0;width:1200px;height:217px;background:linear-gradient(#3a3a3a 0,#1e1e1e 8px,#161616 100%);border-top:6px solid #555}
.util-links{right:36px;top:12px;font-size:15px;color:#ddd}
.util-links span{padding:0 6px}
.brand{left:32px;top:36px;font-family:"Ubuntu",sans-serif;font-size:48px;font-weight:400;color:#fff;letter-spacing:1px}
.tagline{left:42px;top:94px;font-size:14px;font-weight:600;color:#fff}
.main-nav{left:0;top:157px;height:54px;display:flex}
.main-nav a{color:#fff;text-decoration:none;font-family:"Ubuntu",sans-serif;font-size:18px;line-height:54px;text-align:center;border-right:1px solid #444}
.search{left:918px;top:153px;width:262px;height:36px;background:#2f2f2f;border-radius:4px;font-size:13px;color:#888;padding:9px 14px}
.search svg{position:absolute;right:12px;top:9px}

/* hero */
.hero{left:0;top:217px;width:1200px;height:495px;background:linear-gradient(180deg,#7fb0e0 0%,#a9c7d8 30%,#6f7a66 55%,#3b3b3a 100%)}

/* main card */
.blog-card{left:22px;top:670px;width:828px;height:1211px;background:var(--card)}
.blog-card .accent{position:absolute;left:0;top:0;width:401px;height:6px;background:var(--red)}
.blog-card .accent-rest{position:absolute;left:401px;top:0;width:427px;height:6px;background:#e2e2e2}
.section-title{left:24px;top:36px;font-family:"Ubuntu",sans-serif;font-size:22px;font-weight:400;color:#222}
.title-rule{left:24px;top:75px;width:782px;height:1px;background:#cfcfcf}
.post-date{font-family:"Ubuntu",sans-serif;font-size:19px;color:var(--red)}
.thumb{background:linear-gradient(135deg,#4c5a3a,#2c2c2c 55%,#8a8f93)}
.thumb.light{background:linear-gradient(135deg,#d9dcdc,#8f9498 60%,#3b3d3f)}
.lead{font-size:16px;font-weight:600;color:#111;line-height:23px}
.body-text{font-size:13.5px;line-height:23px;color:#444}
.dots{height:0;border-top:1px dotted #999}
.learn{font-size:17px;color:#222}

/* sidebar */
.panel-head{left:867px;width:313px;height:49px;background:var(--panel-head);font-family:"Ubuntu",sans-serif;font-size:19px;color:#333;padding:12px 26px}
.panel-head svg{position:absolute;right:0;bottom:-14px}
.weather-row{left:867px;width:307px;height:65px;background:#fff}
.weather-row svg{position:absolute;left:4px;top:4px}
.weather-row .mm{position:absolute;left:96px;top:10px;font-size:14px;line-height:24px;color:#555}
.weather-row .sep{position:absolute;left:181px;top:10px;width:1px;height:45px;background:#ccc}
.weather-row .mw{position:absolute;left:198px;top:10px;font-size:14px;line-height:24px;color:#555}
.calendar{left:873px;top:1101px;width:306px;height:262px;background:var(--cal-red);border:3px solid var(--cal-border)}
.cal-head{position:absolute;left:0;top:8px;width:100%;text-align:center;font-family:"Ubuntu",sans-serif;font-size:19px;color:#f5c9cf}
.cal-head .prev{position:absolute;left:12px}
.cal-head .next{position:absolute;right:12px}
.cal-grid{position:absolute;left:11px;top:49px;display:grid;grid-template-columns:repeat(7,38px);column-gap:3px;row-gap:0}
.cal-grid .dow{height:29px;margin:0 4px 6px;background:var(--yellow);color:#3a1a00;font-weight:600;font-size:16px;text-align:center;line-height:29px}
.cal-grid .d{height:30px;text-align:center;color:#fff;font-size:16px;line-height:30px}
.event{left:877px;width:275px}
.event h4{font-size:14.5px;font-weight:600;color:#222}
.event p{font-size:14.5px;line-height:21px;color:#444}
.event .more{display:block;font-size:15.5px;color:#222;margin-top:8px}
.btn-more{left:1076px;top:1816px;width:96px;height:29px;background:#262626;border-radius:3px;color:#fff;font-size:13px;text-align:center;line-height:29px}

/* footer */
.site-footer{left:0;top:1866px;width:1200px;height:457px;background:linear-gradient(#2b2b2b,#101010)}
.foot-title{font-family:"Ubuntu",sans-serif;font-size:20px;color:#fff}
.foot-divider{width:1px;background:#3e3e3e}
.quick-list{list-style:none;font-size:14.5px;color:var(--foot-text)}
.quick-list li{height:33px}
.quick-list li::before{content:"›";margin-right:8px;color:#fff}
.tweet{left:474px;width:350px;font-size:14px;line-height:21px;color:var(--foot-text);font-style:italic}
.tweet b{font-weight:600;color:#fff}
.tweet .when{display:block;margin-top:8px;font-style:normal;color:var(--foot-muted)}
.social{left:915px;display:flex;gap:14px}
.social span{width:32px;height:32px;border-radius:50%;background:#fff}
.copyright{left:42px;font-size:14px;color:#777}
</style>
</head>
<body>

<header class="site-header abs">
  <div class="util-links abs">Dashboard<span>|</span>Sign Out<span>|</span>Log In</div>
  <div class="brand abs">TEAM KORVEL</div>
  <div class="tagline abs">When the going gets tough, the tough get...e pinke!</div>
  <nav class="main-nav abs">
    <a style="width:147px">About</a>
    <a style="width:229px">Upcoming Events</a>
    <a style="width:187px">Recent Blog</a>
    <a style="width:176px">Create Blog</a>
    <a style="width:120px;border-right:none">Contact</a>
  </nav>
  <div class="search abs">enter keyword
    <svg width="18" height="18" viewBox="0 0 18 18"><circle cx="7.5" cy="7.5" r="5.5" fill="none" stroke="#ddd" stroke-width="2.2"/><line x1="11.5" y1="11.5" x2="16" y2="16" stroke="#ddd" stroke-width="2.6"/></svg>
  </div>
</header>

<div class="hero abs" role="img" aria-label="Team cyclists in matching kit standing with their road bikes in a car park"></div>

<main class="blog-card abs">
  <div class="accent"></div><div class="accent-rest"></div>
  <h2 class="section-title abs">Recent Blog Post</h2>
  <div class="title-rule abs"></div>

  <article>
    <div class="post-date abs" style="left:24px;top:96px">Tuesday 20 August 2012</div>
    <div class="thumb abs" style="left:24px;top:130px;width:308px;height:164px" role="img" aria-label="Riders on a forest trail ride"></div>
    <div class="abs" style="left:351px;top:128px;width:452px">
      <p class="lead">Lorem ipsum dolor sit amet, consectetuer adipiscing elit. Nam cursus. Morbi ut mi.</p>
      <p class="body-text">Nullam enim leo, egestas id, condimentum at, laoreet mattis, massa. Sed eleifend nonummy diam. Praesent mauris ante, elementum et, bibendum at, posuere sit amet, nibh. Pellentesque habitant morbi tristique senectus et netus et malesuada fames ac turpis egestas. In posuere felis nec tortor. Pellentesque faucibus. Ut accumsan ultricies elit. Maecenas at justo id velit</p>
    </div>
    <p class="body-text abs" style="left:24px;top:305px;width:790px">placerat molestie. Donec dictum lectus non odio. Cras a ante vitae enim iaculis aliquam. Mauris nunc quam, venenatis nec, euismod sit amet, egestas placerat, est. Pellentesque habitant morbi tristique senectus et netus et malesuada fames ac turpis egestas. Cras id elit. Integer quis urna. Ut ante enim, dapibus malesuada, fringilla eu, condimentum quis, tellus. Aenean porttitor eros vel dolor. Donec convallis pede venenatis nibh. Duis quam. Nam eget lacus.</p>
    <div class="dots abs" style="left:26px;top:421px;width:794px"></div>
  </article>

  <article>
    <div class="post-date abs" style="left:26px;top:442px">Monday 10 August 2012</div>
    <div class="thumb light abs" style="left:26px;top:479px;width:203px;height:164px" role="img" aria-label="Close-up of a bike frame with written initials"></div>
    <div class="abs" style="left:250px;top:476px;width:560px">
      <p class="lead">Lorem ipsum dolor sit amet, consectetuer adipiscing elit. Nam cursus. Morbi ut mi.</p>
      <p class="body-text">Nullam enim leo, egestas id, condimentum at, laoreet mattis, massa. Sed eleifend nonummy diam. Praesent mauris ante, elementum et, bibendum at, posuere sit amet, nibh. Pellentesque habitant morbi tristique senectus et netus et malesuada fames ac turpis egestas. In posuere felis nec tortor. Pellentesque faucibus. Ut accumsan ultricies elit. Maecenas at justo id velit</p>
    </div>
    <p class="body-text abs" style="left:26px;top:652px;width:790px">placerat molestie. Donec dictum lectus non odio. Cras a ante vitae enim iaculis aliquam. Mauris nunc quam, venenatis nec, euismod sit amet, egestas placerat, est. Pellentesque habitant morbi tristique senectus et netus et malesuada fames ac turpis egestas. 3</p>
    <div class="dots abs" style="left:26px;top:733px;width:794px"></div>
  </article>

  <article>
    <div class="post-date abs" style="left:26px;top:752px">Friday 01 August 2012</div>
    <div class="thumb abs" style="left:26px;top:788px;width:203px;height:164px" role="img" aria-label="Riders pushing bikes through woodland"></div>
    <div class="abs" style="left:250px;top:786px;width:560px">
      <p class="lead">Lorem ipsum dolor sit amet, consectetuer adipiscing elit. Nam cursus. Morbi ut mi.</p>
      <p class="body-text">Nullam enim leo, egestas id, condimentum at, laoreet mattis, massa. Sed eleifend nonummy diam. Praesent mauris ante, elementum et, bibendum at, posuere sit amet, nibh. Pellentesque habitant morbi tristique senectus et netus et malesuada fames ac turpis egestas. In posuere felis nec tortor. Pellentesque faucibus. Ut accumsan ultricies elit. Maecenas at justo id velit</p>
    </div>
    <p class="body-text abs" style="left:24px;top:962px;width:792px">Mauris vel lacus vitae felis vestibulum volutpat. Etiam est nunc, venenatis in, tristique eu, imperdiet ac, nisl. Cum sociis natoque penatibus et magnis dis parturient montes, nascetur ridiculus mus. In iaculis facilisis massa. Etiam eu urna. Sed porta. Suspendisse quam leo, molestie sed, luctus quis, feugiat in, pede. Fusce tellus. Sed metus augue, convallis et, vehicula ut, pulvinar eu, ante. Integer orci tellus, tristique vitae, consequat nec, porta vel, lectus. Nulla sit amet diam. Duis non nunc. Nulla rhoncus dictum metus. Curabitur tristique mi condimentum orci. Phasellus pellentesque aliquam enim. Proin dui lectus, cursus eu, mattis laoreet, viverra sit amet, quam. Curabitur vel dolor ultrices ipsum dictum tristique. Praesent vitae lacus. Ut velit enim, vestibulum non, fermentum nec, hendrerit quis, leo. Pellentesque rutrum malesuada neque.</p>
    <div class="dots abs" style="left:26px;top:1149px;width:794px"></div>
    <div class="learn abs" style="left:30px;top:1159px">learn more ›</div>
  </article>
</main>

<aside>
  <div class="panel-head abs" style="top:725px">Weather Report
    <svg width="40" height="14" viewBox="0 0 40 14"><polygon points="0,0 40,0 22,14" fill="#d9d9d9"/></svg></div>

  <div class="weather-row abs" style="top:794px">
    <svg width="80" height="58" viewBox="0 0 80 58"><rect width="80" height="58" fill="#cfe6f3"/><circle cx="42" cy="24" r="13" fill="#f5c21a"/><ellipse cx="34" cy="40" rx="22" ry="10" fill="#3a3a3a"/></svg>
    <div class="mm">Min: 69 °F<br>Max: 80 °F</div><div class="sep"></div><div class="mw">Moisture: 68%<br>Wind: 19 Mph</div>
  </div>
  <div class="weather-row abs" style="top:867px">
    <svg width="80" height="58" viewBox="0 0 80 58"><ellipse cx="40" cy="24" rx="28" ry="14" fill="#3a3a3a"/><g stroke="#3a3a3a" stroke-width="2"><line x1="22" y1="42" x2="18" y2="52"/><line x1="34" y1="42" x2="30" y2="54"/><line x1="46" y1="42" x2="42" y2="54"/><line x1="58" y1="42" x2="54" y2="52"/></g></svg>
    <div class="mm">Min: 69 °F<br>Max: 80 °F</div><div class="sep"></div><div class="mw">Moisture: 68%<br>Wind: 19 Mph</div>
  </div>
  <div class="weather-row abs" style="top:940px">
    <svg width="80" height="58" viewBox="0 0 80 58"><circle cx="42" cy="24" r="13" fill="#f5c21a"/><ellipse cx="34" cy="40" rx="22" ry="10" fill="#3a3a3a"/></svg>
    <div class="mm">Min: 69 °F<br>Max: 80 °F</div><div class="sep"></div><div class="mw">Moisture: 68%<br>Wind: 19 Mph</div>
  </div>

  <div class="panel-head abs" style="top:1033px">Our Calendar
    <svg width="40" height="14" viewBox="0 0 40 14"><polygon points="0,0 40,0 22,14" fill="#d9d9d9"/></svg></div>

  <div class="calendar abs">
    <div class="cal-head"><span class="prev">‹</span>March 2012<span class="next">›</span></div>
    <div class="cal-grid">
      <div class="dow">M</div><div class="dow">T</div><div class="dow">W</div><div class="dow">T</div><div class="dow">F</div><div class="dow">S</div><div class="dow">S</div>
      <div class="d"></div><div class="d"></div><div class="d"></div><div class="d">1</div><div class="d">2</div><div class="d">3</div><div class="d">4</div>
      <div class="d">5</div><div class="d">6</div><div class="d">7</div><div class="d">8</div><div class="d">9</div><div class="d">10</div><div class="d">11</div>
      <div class="d">12</div><div class="d">13</div><div class="d">14</div><div class="d">15</div><div class="d">16</div><div class="d">17</div><div class="d">18</div>
      <div class="d">19</div><div class="d">20</div><div class="d">21</div><div class="d">22</div><div class="d">23</div><div class="d">24</div><div class="d">25</div>
      <div class="d">26</div><div class="d">27</div><div class="d">28</div><div class="d">29</div><div class="d">30</div><div class="d">31</div><div class="d"></div>
    </div>
  </div>

  <div class="panel-head abs" style="top:1382px">Upcoming Events
    <svg width="40" height="14" viewBox="0 0 40 14"><polygon points="0,0 40,0 22,14" fill="#d9d9d9"/></svg></div>

  <div class="event abs" style="top:1446px">
    <h4>Event Name here | 20 Aug 2012</h4>
    <p>Lorem ipsum dolor sit amet, consectetuer adipiscing elit. Nam cursus. Morbi ut mi. Nullam enim leocondimentum at, laoreet mattis, massa.</p>
    <span class="more">learn more</span>
  </div>
  <div class="event abs" style="top:1598px">
    <h4>Event Name here | 20 Aug 2012</h4>
    <p>Lorem ipsum dolor sit amet, consectetuer adipiscing elit.</p>
    <span class="more">learn more</span>
  </div>
  <div class="event abs" style="top:1711px">
    <h4>Event Name here | 20 Aug 2012</h4>
    <p>Lorem ipsum dolor sit amet, consectetuer adipiscing elit.</p>
    <span class="more">learn more</span>
  </div>
  <div class="btn-more abs">view more ›</div>
</aside>

<footer class="site-footer abs">
  <div class="foot-title abs" style="left:50px;top:43px">Quick Links</div>
  <ul class="quick-list abs" style="left:52px;top:96px">
    <li>Home</li><li>About Us</li><li>Recent Blog</li><li>Social Feed</li><li>Get Connected</li>
  </ul>
  <ul class="quick-list abs" style="left:226px;top:96px">
    <li>Create Blog</li><li>Upcoming Events</li><li>Calendar</li><li>Weather Forecast</li><li>Contact</li>
  </ul>
  <div class="foot-divider abs" style="left:406px;top:20px;height:360px"></div>

  <div class="foot-title abs" style="left:474px;top:43px">Social Feed</div>
  <p class="tweet abs" style="top:86px"><b>Gerald Moon</b> @ Lorem ipsum dolor sit amet, consectetuer adipiscing elit. Nam cursus. Morbi ut mi.<span class="when">Posted on 23 Aug 2012</span></p>
  <p class="tweet abs" style="top:170px"><b>Jim Porter</b> @ Lorem ipsum dolor sit amet, consectetuer adipiscing elit. Nam cursus. Morbi ut mi. Nullam enim<span class="when">Posted on 23 Aug 2012</span></p>
  <p class="tweet abs" style="top:263px"><b>Kara Wilde</b> @ Lorem ipsum dolor sit amet, consectetuer adipiscing elit. Nam cursus. Morbi ut mi.<span class="when">Posted on 23 Aug 2012</span></p>
  <div class="foot-divider abs" style="left:850px;top:20px;height:360px"></div>

  <div class="foot-title abs" style="left:913px;top:43px">Get Connected</div>
  <div class="social abs" style="top:86px"><span></span><span></span><span></span><span></span></div>

  <div class="foot-divider abs" style="left:36px;top:382px;width:1126px;height:1px"></div>
  <div class="copyright abs" style="top:406px">© 2012 Company Name &nbsp;|&nbsp; Privacy Policy &nbsp;|&nbsp; Term &amp; Conditions</div>
</footer>

</body>
</html>
```